The Harlow Law Firm, PC

Dwight K. Harlow
Attorney at Law
physical address: 728 E. 9th Avenue
Greenville, NC 27561

mailing: P.O. Box 5873
Greenville, NC 27563

o. 252.431.6672
f. 252.431.8815

www.harlowlegal-example.com

Industry/Entity Type

Attorney

Contact Information for Business Card

Attorney name
Office Phone number
Office Fax number
Mailing address and physical address
website address

Requirements
Must have
• Clean fresh design - I hate the website

```html
<!DOCTYPE html>
<html lang="en">
<head>
<meta charset="utf-8">
<title>Dwight K. Harlow – Attorney at Law Business Card</title>
<link href="https://fonts.googleapis.com/css2?family=Pinyon+Script&family=Jost:wght@500&family=Marcellus&display=swap" rel="stylesheet">
<style>
  :root {
    --page-bg: #e6e6e6;
    --card-bg: #ffffff;
    --burgundy-deep: #6e0710;
    --burgundy-mid: #8e141c;
    --text-burgundy: #7a0a12;
    --gold: #d4a640;
    --name-ink: #222222;
  }
  html, body {
    margin: 0;
    padding: 0;
    width: 1200px;
    height: 1000px;
    overflow: hidden;
    background: var(--page-bg);
  }
  .business-card {
    position: absolute;
    left: 173px;
    top: 248px;
    width: 846px;
    height: 468px;
    background: var(--card-bg);
  }
  .title-ribbon {
    position: absolute;
    left: 30px;
    top: 0;
    width: 158px;
    height: 454px;
  }
  .ribbon-label {
    position: absolute;
    left: 30px;
    top: 348px;
    width: 158px;
    text-align: center;
    font-family: "Marcellus", serif;
    font-size: 22px;
    line-height: 30px;
    color: var(--gold);
    letter-spacing: 0.2px;
  }
  .attorney-name {
    position: absolute;
    left: 224px;
    top: 152px;
    width: 578px;
    margin: 0;
    text-align: center;
    font-family: "Pinyon Script", cursive;
    font-weight: 400;
    font-size: 68px;
    line-height: 80px;
    color: var(--name-ink);
  }
  .name-rule {
    position: absolute;
    left: 224px;
    top: 239px;
    width: 578px;
    height: 2px;
    background: var(--text-burgundy);
  }
  .contact-details {
    position: absolute;
    right: 43px;
    top: 316px;
    margin: 0;
    text-align: right;
    font-family: "Jost", sans-serif;
    font-weight: 500;
    font-size: 19px;
    line-height: 27.5px;
    color: var(--text-burgundy);
    white-space: pre;
  }
  .edge-tab {
    position: absolute;
    right: 0;
    top: 318px;
    width: 27px;
    height: 100px;
    background: var(--burgundy-deep);
  }
</style>
</head>
<body>
  <div class="business-card">
    <svg class="title-ribbon" viewBox="0 0 158 454" aria-hidden="true">
      <defs>
        <linearGradient id="ribbonShade" x1="0" y1="0" x2="0" y2="1">
          <stop offset="0" stop-color="#6a0610"/>
          <stop offset="0.45" stop-color="#8e141c"/>
          <stop offset="1" stop-color="#6a0610"/>
        </linearGradient>
      </defs>
      <polygon points="1,0 157,0 157,420 79,452 1,420" fill="url(#ribbonShade)" stroke="#d4a640" stroke-width="2"/>
    </svg>
    <div class="ribbon-label">ATTORNEY<br>AT LAW</div>

    <h1 class="attorney-name">Dwight K. Harlow</h1>
    <div class="name-rule"></div>

    <p class="contact-details">physical address: 728 E. 9th Avenue  Greenville, NC 27561
mailing: P.O. Box 5873   Greenville, NC 27563
o. 252.431.6672   f. 252.431.8815
www.harlowlegal-example.com</p>
    <div class="edge-tab"></div>
  </div>
</body>
</html>
```